Website Design and Build

This is a design and build of a dating site.

100% the most important thing is for the website to look good. I want this thing to be stunning and feel like a premium product so please only tender for the job if you excel at design and use of colours.

Theme is: premium, professional & uncluttered
Colour Scheme is: bright, fun and friendly but also reassuring and professional
 
Platforms: Initially just browser based (desktop and mobile) but if the proof of concept works we will roll it out to apps across the major platforms.

Marketing will be done primarily through organic online searches and content driven leads to a squeeze page, so SEO optimisation and experience with squeeze pages also a must.

Please include examples of sites you’ve done or other sites you think give a flavour of your vision for what this site will be. Any thoughts on palettes/colour scheme also useful.

I will provide the full brief to the successful designer.

Thank you for your time.

Industry/Entity Type

Dating

Coding

Coded - Design and coding required

Number of Pages Required

5+ page

Font styles to use
Sans Serif

Colors

Designer to choose colors to be used in the design.

Requirements
Must have
• Professional, Premium and uncluttered look.
• SEO optimisation.
• Squeeze page.
• A way to track different lead sources e.g. some of it will be content led to a squeeze page, some of it organic search engine hits, some of it unique referral links given to specific bloggers/influencers. I want to be able to track the success of all the different types of generating traffic to the site.
• I also want to be able to amend/update the site myself going forward so would like the spec/design to be clearly documented to allow me to do this.

```html
<!DOCTYPE html>
<html lang="en">
<head>
<meta charset="utf-8">
<title>Pairly — Get coupled</title>
<link rel="stylesheet" href="https://fonts.googleapis.com/css2?family=Urbanist:wght@700;800&family=Heebo:wght@400;500;700&display=swap">
<style>
  :root {
    --pink-top: #e597d8;
    --pink-mid: #c274dc;
    --violet: #7a3de6;
    --violet-deep: #5b2fe0;
    --navy: #2b2161;
    --white: #ffffff;
    --lavender: #f3def2;
    --teal: #1fe8cf;
    --rose: #ff5f8f;
    --button-violet: #6a30e8;
  }
  * { box-sizing: border-box; margin: 0; padding: 0; }
  html, body { width: 1200px; height: 900px; overflow: hidden; }
  body { font-family: "Heebo", Arial, sans-serif; }

  .page {
    position: relative;
    width: 1200px;
    height: 900px;
    overflow: hidden;
    background: linear-gradient(165deg, var(--pink-top) 0%, var(--pink-mid) 30%, var(--violet) 65%, var(--violet-deep) 100%);
  }

  .light-band { position: absolute; inset: 0; width: 1200px; height: 900px; }

  /* Header */
  .site-header {
    position: absolute; top: 0; left: 0; right: 0; height: 100px;
    display: flex; align-items: center; padding: 0 22px 0 18px;
    z-index: 3;
  }
  .brand { display: flex; align-items: center; gap: 12px; margin-right: 40px; }
  .brand-dot {
    width: 56px; height: 56px; border-radius: 50%;
    background: var(--white);
    box-shadow: 0 0 0 8px rgba(255,255,255,0.3);
  }
  .brand-name {
    font-family: "Urbanist", Arial, sans-serif; font-weight: 800;
    font-size: 20px; color: var(--navy);
  }
  .utility-nav { display: flex; align-items: center; gap: 24px; }
  .utility-nav a, .main-nav a {
    font-size: 15px; font-weight: 500; text-decoration: none; letter-spacing: 0.02em;
    white-space: nowrap;
  }
  .utility-nav a { color: var(--navy); display: flex; align-items: center; gap: 8px; }
  .main-nav { margin-left: auto; display: flex; align-items: center; gap: 30px; }
  .main-nav a { color: var(--white); }
  .main-nav a.is-active { color: var(--teal); }
  .main-nav .login-button {
    background: var(--button-violet); color: var(--white);
    font-size: 12px; font-weight: 700;
    padding: 8px 24px; border-radius: 4px; margin-left: 12px;
  }

  /* Hero */
  .hero-copy { position: absolute; left: 99px; top: 272px; z-index: 3; }
  .hero-title {
    font-family: "Urbanist", Arial, sans-serif; font-weight: 800;
    font-size: 68px; line-height: 84px; color: var(--white);
    white-space: nowrap; letter-spacing: -0.01em;
  }
  .hero-title .accent { color: var(--teal); }
  .hero-lead {
    margin-top: 26px; font-size: 19px; line-height: 22px;
    color: var(--white); font-weight: 400; white-space: nowrap;
  }
  .hero-actions { margin-top: 52px; display: flex; align-items: center; gap: 26px; }
  .button {
    display: inline-flex; align-items: center; justify-content: center;
    height: 50px; width: 190px; padding: 0 10px; border-radius: 5px;
    font-size: 15px; font-weight: 700; letter-spacing: 0.05em;
    text-decoration: none; text-transform: uppercase; white-space: nowrap;
  }
  .button-primary { background: var(--teal); color: #3a2a8a; }
  .button-outline { border: 2px solid var(--rose); color: var(--white); }
  .hero-actions .or { color: var(--white); font-weight: 700; font-size: 15px; }

  .hero-illustration {
    position: absolute; left: 760px; top: 228px; width: 350px; height: 600px;
    border-radius: 44px;
    background: linear-gradient(160deg, #8a5cf0 0%, #6a30e8 45%, #e8479a 80%, #f2b233 100%);
    z-index: 2;
  }

  .scroll-cue { position: absolute; left: 649px; top: 846px; z-index: 2; }
</style>
</head>
<body>
<div class="page">
  <svg class="light-band" viewBox="0 0 1200 900" aria-hidden="true">
    <polygon points="1082,0 1200,0 1200,900 442,900" fill="#ffffff"/>
    <polygon points="1200,450 1200,900 929,900" fill="var(--lavender)"/>
  </svg>

  <header class="site-header">
    <div class="brand">
      <span class="brand-dot"></span>
      <span class="brand-name">Pairly</span>
    </div>
    <nav class="utility-nav">
      <a href="#"><svg width="15" height="15" viewBox="0 0 16 16" aria-hidden="true"><circle cx="6.5" cy="6.5" r="5" fill="none" stroke="currentColor" stroke-width="2.2"/><line x1="10.5" y1="10.5" x2="15" y2="15" stroke="currentColor" stroke-width="2.4" stroke-linecap="round"/></svg>SEARCH</a>
      <a href="#">DOWNLOADS</a>
    </nav>
    <nav class="main-nav">
      <a href="#" class="is-active">HOME</a>
      <a href="#">NEWS</a>
      <a href="#">COUPLES</a>
      <a href="#" class="login-button">LET ME IN</a>
    </nav>
  </header>

  <section class="hero-copy">
    <h1 class="hero-title">No more lonely days<br>Get <span class="accent">coupled</span></h1>
    <p class="hero-lead">
      The bright app for people who dream about a perfect match.<br>
      Get in touch, communicate and find the love of your life.<br>
      Let AI help you find your soulmate and plan an ideal date.<br>
      There are no excuses for lonely days any more.
    </p>
    <div class="hero-actions">
      <a href="#" class="button button-primary">Make a profile</a>
      <span class="or">or</span>
      <a href="#" class="button button-outline">Find the couple</a>
    </div>
  </section>

  <div class="hero-illustration" role="img" aria-label="Illustration of a large smartphone with a woman sitting on a bench inside its screen, listening to music, while another woman sits outside the phone looking at her own device"></div>

  <svg class="scroll-cue" width="22" height="38" viewBox="0 0 22 38" aria-label="Scroll down" role="img">
    <rect x="1.5" y="1.5" width="19" height="35" rx="9.5" fill="none" stroke="#8a5cf0" stroke-width="2.5"/>
    <line x1="11" y1="10" x2="11" y2="20" stroke="#8a5cf0" stroke-width="2.5" stroke-linecap="round"/>
  </svg>
</div>
</body>
</html>
```